BrivoMetra. Lantern for the Enterprise Worth. Business card

Professional business card for BrivoMetra (Lantern for the Enterprise Worth)
My rationale: Strategy-> Execution-> Results-> Value that lead to the BrivoMetra name: We put the Lantern for the Enterprise Worth.
We deliver value to our customers helping them at defining a good strategy (cyan arrow). 90% of well formulated strategies fail due to poor execution so we also consider strategical execution very important (green arrow). Due to the execution we obtain the results (blue arrow). Finally, the results provide feedback to redefine strategy, and the new strategy has to be executed and new results obtained providing new feedback and on and on. It's like a wheel that finally, must create corporate value: value for shareholders, staholders, employees, providers...-

Target Market(s)

CEOs and steering comitees , invewrnent funds

Industry/Entity Type

Business Consultant

Contact Information for Business Card

Teodoro Vinschetti
CEO & Founder
teodoro.vinschetti@brivometra-example.com
Mobile: +34 655.802.913
www.brivometra-example.com

Colors

Designer to choose colors to be used in the design.

Requirements
Nice to have
• Nice to hace the words: Strategy, execution, results
• Nice to vave the claim: Lantern for the Enterprise Worth
• The three colors should be shown:
• cyan for STRATEGY
• green for EXECUTION
• blue for RESULTS
Should not have
• Complete black background

```html
<!DOCTYPE html>
<html lang="en">
<head>
<meta charset="utf-8">
<title>BrivoMetra — Business Card</title>
<link rel="stylesheet" href="https://fonts.googleapis.com/css2?family=Source+Sans+3:wght@400;600;700&display=swap">
<style>
  :root {
    --blue: #1f3f94;
    --green: #8cc63f;
    --cyan: #29a3dc;
    --paper: #ffffff;
    --stage-light: #eef1f3;
    --stage-dark: #a9abae;
  }
  * { box-sizing: border-box; margin: 0; padding: 0; }
  html, body { width: 1200px; height: 800px; overflow: hidden; }
  body {
    font-family: "Source Sans 3", "Myriad Pro", sans-serif;
    background: radial-gradient(ellipse at 75% 15%, var(--stage-light), var(--stage-dark) 80%);
    position: relative;
  }
  .card {
    position: absolute;
    left: 320px;
    width: 560px;
    height: 320px;
    background: var(--paper);
    box-shadow: 0 6px 18px rgba(0,0,0,.22);
    overflow: hidden;
  }
  .card--front { top: 50px; }
  .card--back { top: 420px; }

  .colour-band {
    position: absolute; left: 0; right: 0; bottom: 0; height: 12px;
    display: flex;
  }
  .colour-band span:nth-child(1) { flex: 30; background: var(--blue); }
  .colour-band span:nth-child(2) { flex: 35; background: var(--green); }
  .colour-band span:nth-child(3) { flex: 35; background: var(--cyan); }

  /* front */
  .front-mark {
    position: absolute; top: 92px; left: 0; right: 0;
    display: flex; align-items: center; justify-content: center; gap: 14px;
  }
  .mark-dot { width: 26px; height: 26px; border-radius: 50%; background: var(--blue); }
  .brand-name {
    font-weight: 700; color: var(--blue); letter-spacing: -0.5px;
  }
  .front-mark .brand-name { font-size: 50px; }
  .tagline {
    position: absolute; top: 196px; left: 0; right: 0; text-align: center;
    font-weight: 700; font-size: 20px; color: var(--blue);
    text-transform: uppercase; letter-spacing: 0.3px;
  }

  /* back */
  .back-brand {
    position: absolute; left: 34px; top: 118px;
    display: flex; align-items: center; gap: 10px;
  }
  .back-brand .mark-dot { width: 18px; height: 18px; }
  .back-brand .brand-name { font-size: 38px; }
  .divider {
    position: absolute; left: 248px; top: 92px; width: 2px; height: 118px;
    background: linear-gradient(var(--blue) 0 33%, var(--green) 33% 66%, var(--cyan) 66% 100%);
  }
  .contact {
    position: absolute; left: 266px; top: 94px; color: var(--blue);
  }
  .person-name { font-weight: 700; font-size: 22px; line-height: 1.05; }
  .person-role { font-size: 16px; color: var(--cyan); margin-bottom: 14px; }
  .contact-list { list-style: none; font-size: 14.5px; line-height: 1.35; }
  .contact-list li { display: flex; align-items: center; gap: 6px; }
  .contact-list svg { width: 13px; height: 13px; flex: none; }
</style>
</head>
<body>

<section class="card card--front" aria-label="Business card front">
  <div class="front-mark">
    <span class="mark-dot"></span>
    <span class="brand-name">BrivoMetra</span>
  </div>
  <p class="tagline">Lantern for the Enterprise Worth</p>
  <div class="colour-band"><span></span><span></span><span></span></div>
</section>

<section class="card card--back" aria-label="Business card back">
  <div class="back-brand">
    <span class="mark-dot"></span>
    <span class="brand-name">BrivoMetra</span>
  </div>
  <div class="divider"></div>
  <div class="contact">
    <p class="person-name">Teodoro Vinschetti</p>
    <p class="person-role">CEO &amp; Founder</p>
    <ul class="contact-list">
      <li>
        <svg viewBox="0 0 14 14" aria-hidden="true"><rect x="3.5" y="1" width="7" height="12" rx="1.2" fill="none" stroke="#8cc63f" stroke-width="1.2"/><line x1="6" y1="11" x2="8" y2="11" stroke="#8cc63f" stroke-width="1.2"/></svg>
        +34 655.802.913
      </li>
      <li>
        <svg viewBox="0 0 14 14" aria-hidden="true"><rect x="1" y="3" width="12" height="8" fill="none" stroke="#8cc63f" stroke-width="1.2"/><polyline points="1,3 7,8 13,3" fill="none" stroke="#8cc63f" stroke-width="1.2"/></svg>
        teodoro.vinschetti@brivometra-example.com
      </li>
      <li>
        <svg viewBox="0 0 14 14" aria-hidden="true"><circle cx="7" cy="7" r="5.8" fill="none" stroke="#8cc63f" stroke-width="1.2"/><ellipse cx="7" cy="7" rx="2.5" ry="5.8" fill="none" stroke="#8cc63f" stroke-width="1"/><line x1="1.2" y1="7" x2="12.8" y2="7" stroke="#8cc63f" stroke-width="1"/></svg>
        www.brivometra-example.com
      </li>
    </ul>
  </div>
  <div class="colour-band"><span></span><span></span><span></span></div>
</section>

</body>
</html>
```